Business Card Design Project

We need a business card design for a company based in San Diego California named "KBDMasonry Inc." We are dedicated installers of fireplaces, pre cast concrete, stone masonry. We also pecialice in block construction.
Updates

Thank you very much guys, very good designs so far although I would like to point out that the front should have: Company name, license number, and please tell me if a Qr code is too much (if it isn't then it should be in a bottom corner. <img src="http://qr.codelyft.net/?l=1&s=8&d=BEGIN:VCARD%0AVERSION:2.1%0AN:Herrera;Tomas+%0AFN:Tomas++Herrera%0ATEL;WORK;VOICE:17609135246%0AEMAIL;WORK;INTERNET:kbdmasonry%40mailbrook.net%0AURL:www.kbdmasonry.net%0AORG:KBD+Masonry+Inc%0ATITLE:Contractor%0AADR;WORK:;;;Oceanside;California;92058;USA%0AEND:VCARD" alt="QRCode"/>  Or I'll upload the picture.

Also we are currently constructing our website, there you can find pictures of what we do. 
kbdmasonry.net 
Thank you guys again.

Industry/Entity Type

Business

Requirements
Must have
• Company name: K B D Masonry Inc
Licence number: 482913
Tomas Herrera Villa
Phone number: 7670 555 0142
Nice to have
• We would like to have an image that represents the business area of work; a fireplace, a fountain, a balcony, a niche, an arch.

```html
<!DOCTYPE html>
<html lang="en">
<head>
<meta charset="utf-8">
<title>K B D Masonry Inc — Business Card</title>
<link rel="stylesheet" href="https://fonts.googleapis.com/css2?family=Source+Sans+3:wght@400;500&family=Vollkorn:wght@600&display=swap">
<style>
  :root {
    --card-base: #ececec;
    --card-light: #f6f6f6;
    --card-shade: #dedede;
    --panel: rgba(190, 190, 190, 0.42);
    --mark: #8a8a8a;
    --brand-text: #2e2e2e;
    --title: #5a5a5a;
    --label: #e8762b;
    --value: #3f3f3f;
  }
  * { box-sizing: border-box; margin: 0; padding: 0; }
  html, body { width: 1200px; height: 720px; overflow: hidden; }
  body { font-family: "Source Sans 3", "Helvetica Neue", Arial, sans-serif; }

  .card {
    position: relative;
    width: 1200px;
    height: 720px;
    overflow: hidden;
    background:
      radial-gradient(ellipse at 30% 25%, var(--card-light) 0%, transparent 60%),
      radial-gradient(ellipse at 80% 85%, var(--card-shade) 0%, transparent 55%),
      var(--card-base);
  }

  .band-left {
    position: absolute;
    left: 0; top: 163px;
    width: 108px; height: 394px;
    background: var(--panel);
    border-radius: 0 24px 24px 0;
  }
  .band-right {
    position: absolute;
    left: 487px; top: 163px;
    width: 713px; height: 394px;
    background: var(--panel);
    border-radius: 24px 0 0 24px;
  }

  .brand {
    position: absolute;
    left: 187px; top: 200px;
    width: 250px;
    text-align: center;
  }
  .brand-mark { display: block; margin: 0 auto; }
  .brand-name {
    margin-top: 46px;
    font-family: "Vollkorn", Georgia, serif;
    font-weight: 600;
    font-size: 49px;
    letter-spacing: 1px;
    color: var(--brand-text);
    line-height: 1;
  }

  .details {
    position: absolute;
    left: 571px; top: 214px;
  }
  .company-title {
    font-size: 57px;
    font-weight: 400;
    color: var(--title);
    letter-spacing: -0.5px;
    line-height: 1;
    margin-bottom: 22px;
  }
  .detail-line {
    font-size: 29px;
    line-height: 45px;
    color: var(--value);
  }
  .detail-label { color: var(--label); }
</style>
</head>
<body>
  <main class="card">
    <div class="band-left"></div>
    <div class="band-right"></div>

    <div class="brand">
      <svg class="brand-mark" width="130" height="130" viewBox="0 0 130 130" aria-hidden="true">
        <circle cx="65" cy="65" r="62" fill="var(--mark)"/>
      </svg>
      <p class="brand-name">Company</p>
    </div>

    <section class="details">
      <h1 class="company-title">K B D MASONRY INC</h1>
      <p class="detail-line"><span class="detail-label">Licence number</span> 482913</p>
      <p class="detail-line">Tomas Herrera Villa</p>
      <p class="detail-line"><span class="detail-label">Phone number</span> 7670 555 0142</p>
      <p class="detail-line"><span class="detail-label">Email</span> name@kbdmasonry.net</p>
      <p class="detail-line"><span class="detail-label">Url</span> kbdmasonry.net</p>
    </section>
  </main>
</body>
</html>
```